Corporate flyer highlighting service offering for PR agency

A corporate flyer is needed for a new service offering that we are doing. The product name is SaleNimbus it is a marketing and communications services offering for companies who are getting ready to sell their business. If we are really happy with the designer's work, there will be a great deal more projects. I am looking for a clean design with a few pops of color from my site. https://brightmoorlane.partners. I am looking for a good design with data in sections. I am looking for a clean design that feels high-end but not cluttered. Please do not use images of people. Please see the following examples of types of designs I like.
https://www.pinboardia.example/pin/830172649205518834/
https://www.pinboardia.example/pin/391827465019283745/
https://assets.tovarnel.example/corporate-flyer-template-KQPMRT
https://artbrookly.example/item/corporate-flyer-template/48193726?s_rank=8
https://assets.tovarnel.example/corporate-business-flyer-template-83VN2L
Updates

I had to place the project on hold as I choose the wrong type of project and did not get many designs as a result. I am reposting this with an updated brief.

Target Market(s)

Business sellers and brokers

Industry/Entity Type

Marketing for business sellers

Font styles to use
Sans Serif

Requirements
Must have
• Good quality design with content in sections. Clean and high end feeling is a must.
Should not have
• A lot of images of people.

```html
<!DOCTYPE html>
<html lang="en">
<head>
<meta charset="utf-8">
<title>SaleNimbus – Increasing Valuation</title>
<link rel="stylesheet" href="https://fonts.googleapis.com/css2?family=Poppins:wght@400;500&family=Exo+2:wght@500;700&display=swap">
<style>
  :root {
    --page-bg: #e8eff6;
    --ink: #1f2a33;
    --muted: #707780;
    --rule: #a3a8ae;
    --tab: #a9adb2;
    --panel-dark: #0c1a26;
    --panel-mid: #1c2c39;
    --hub: #2a3a46;
    --orange: #f15a29;
    --blue: #2d8fd8;
    --green: #7cc242;
    --amber: #f7a21b;
    --white: #ffffff;
  }
  * { margin: 0; padding: 0; box-sizing: border-box; }
  html, body { width: 928px; height: 1200px; overflow: hidden; }
  body {
    background: var(--page-bg);
    position: relative;
    font-family: "Poppins", sans-serif;
    color: var(--ink);
  }
  .intro {
    position: absolute;
    top: 108px;
    left: 109px;
    width: 709px;
    display: flex;
    justify-content: space-between;
    font-size: 16px;
    line-height: 25px;
  }
  .intro-column { width: 328px; text-align: justify; }
  .intro-column--left { text-align-last: justify; }
  .valuation-panel {
    position: absolute;
    left: 109px;
    top: 435px;
    width: 713px;
    height: 570px;
    background:
      radial-gradient(ellipse at 30% 75%, rgba(60,80,95,0.35), transparent 60%),
      linear-gradient(160deg, var(--panel-mid) 0%, var(--panel-dark) 45%, var(--panel-mid) 100%);
  }
  .valuation-title {
    position: absolute;
    top: 66px;
    left: 0;
    width: 100%;
    text-align: center;
    font-family: "Exo 2", sans-serif;
    font-weight: 700;
    font-size: 27px;
    color: var(--white);
  }
  .valuation-diagram { position: absolute; left: 0; top: 0; width: 713px; height: 570px; }
  .diagram-label {
    font-family: "Poppins", sans-serif;
    font-size: 25px;
    fill: #e6ebef;
    text-anchor: middle;
  }
  .hub-name {
    font-family: "Exo 2", sans-serif;
    font-weight: 700;
    font-size: 34px;
    fill: var(--white);
    text-anchor: middle;
  }
  .icon { fill: none; stroke: var(--white); stroke-width: 2.5; stroke-linecap: round; stroke-linejoin: round; }
  .footer-rule {
    position: absolute;
    left: 111px;
    top: 1088px;
    width: 708px;
    height: 2px;
    background: var(--rule);
  }
  .footer-url {
    position: absolute;
    right: 124px;
    top: 1103px;
    font-size: 14px;
    color: var(--muted);
  }
  .page-number {
    position: absolute;
    left: 819px;
    top: 1089px;
    width: 54px;
    height: 37px;
    background: var(--tab);
    color: var(--white);
    font-size: 22px;
    line-height: 37px;
    text-align: center;
  }
</style>
</head>
<body>
  <section class="intro">
    <p class="intro-column intro-column--left">Our team of executive-level communications and marketing experts brings deep buy and sell-side experience. We have played critical roles in the acquisition, integration, and disposition process. This deep mix of financial services expertise combined with decades of experience leading internal and external communications and marketing teams gives us a unique perspective on identifying and</p>
    <div class="intro-column">
      <p>unlocking non-financial areas of value before exit.</p>
      <p>While accounting, investment banking teams are hard at work increasing value from a financial perspective, we help organizations enhance their valuation by identifying areas that will appeal most to buyers and ensuring those elements of your business are visible and memorable to those who matter most.</p>
    </div>
  </section>

  <section class="valuation-panel" role="img" aria-label="Dark blurred office backdrop behind a diagram of four ways to increase valuation">
    <svg class="valuation-diagram" viewBox="0 0 1196 956" aria-hidden="true">
      <!-- connectors -->
      <polyline points="230,286 369,286 505,422" fill="none" stroke="var(--orange)" stroke-width="2"/>
      <circle cx="505" cy="422" r="5" fill="var(--orange)"/>
      <polyline points="969,287 827,287 691,423" fill="none" stroke="var(--blue)" stroke-width="2"/>
      <circle cx="691" cy="423" r="5" fill="var(--blue)"/>
      <polyline points="222,664 365,664 500,529" fill="none" stroke="var(--green)" stroke-width="2"/>
      <circle cx="500" cy="529" r="5" fill="var(--green)"/>
      <polyline points="969,671 827,671 692,536" fill="none" stroke="var(--amber)" stroke-width="2"/>
      <circle cx="692" cy="536" r="5" fill="var(--amber)"/>

      <!-- hub -->
      <polygon points="474,478 536,371 660,371 722,478 660,584 536,584" fill="var(--hub)"/>
      <text class="hub-name" x="598" y="490">SaleNimbus</text>

      <!-- value node -->
      <g transform="translate(192,286)">
        <polygon points="-38,0 -19,-34 19,-34 38,0 19,34 -19,34" fill="var(--orange)"/>
        <circle class="icon" cx="2" cy="-12" r="8"/>
        <path class="icon" d="M2 -16 v8 M-18 4 l10 -6 h12 l6 4 h-10 M-18 14 l8 -4 h14 l14 -10"/>
      </g>
      <text class="diagram-label" x="191" y="368">Highlighting value in a</text>
      <text class="diagram-label" x="191" y="398">clear and visible way</text>

      <!-- exit node -->
      <g transform="translate(1008,287)">
        <polygon points="-38,0 -19,-34 19,-34 38,0 19,34 -19,34" fill="var(--blue)"/>
        <rect x="0" y="-18" width="16" height="32" fill="var(--white)"/>
        <circle cx="-12" cy="-14" r="4" fill="var(--white)"/>
        <path class="icon" d="M-12 -8 v12 l-6 10 M-12 4 l6 10 M-20 -2 l8 -4 l8 4"/>
        <path d="M3 -2 h8 M7 -6 l4 4 l-4 4" fill="none" stroke="var(--blue)" stroke-width="2"/>
      </g>
      <text class="diagram-label" x="1007" y="368">Streamlining the exit</text>
      <text class="diagram-label" x="1007" y="398">process</text>

      <!-- risk node -->
      <g transform="translate(183,664)">
        <polygon points="-38,0 -19,-34 19,-34 38,0 19,34 -19,34" fill="var(--green)"/>
        <path class="icon" d="M0 -20 L20 14 H-20 Z M0 -6 v10 M0 9 v1"/>
      </g>
      <text class="diagram-label" x="182" y="736">Identifying and</text>
      <text class="diagram-label" x="182" y="766">mitigating potential</text>
      <text class="diagram-label" x="182" y="796">risks</text>

      <!-- presence node -->
      <g transform="translate(1009,671)">
        <polygon points="-38,0 -19,-34 19,-34 38,0 19,34 -19,34" fill="var(--amber)"/>
        <path class="icon" d="M-12 -8 h24 l8 8 l-20 20 l-20 -20 Z M-20 0 h40 M-6 -8 l-4 8 l10 20 l10 -20 l-4 -8 M0 -22 v6 M-10 -19 l3 5 M10 -19 l-3 5"/>
      </g>
      <text class="diagram-label" x="1008" y="741">Creating a polished</text>
      <text class="diagram-label" x="1008" y="771">presence in the</text>
      <text class="diagram-label" x="1008" y="801">market ahead of buyer</text>
      <text class="diagram-label" x="1008" y="831">interest</text>
    </svg>
    <h2 class="valuation-title">We help companies increase valuation by:</h2>
  </section>

  <footer>
    <div class="footer-rule"></div>
    <span class="footer-url">https://brightmoorlane.partners</span>
    <span class="page-number">2</span>
  </footer>
</body>
</html>
```